Wedding Startup Full Website Design

We've just completed our online platform and need to create a website that represents our brand and vision, and clearly communicates our features and value proposition to potential users. There are a minimum of 4 pages that need to be designed. One geared toward wedding professionals (venues/vendors/coordinators), another toward engaged couples, one showcasing features, and an 'About Us' page.

The designer will creative freedom to create a unique UI/UX as long as it represents our brand and is relevant to our target audience/market. The ideal candidate will be able to assume the mindset of someone working in the wedding industry and/or an engaged couple. Ability to create illustrations is a plus.

Copy will be provided as needed. We will reimburse for stock images (pending approval before purchasing), but sourcing the stock images will be the responsibility of the designer.

Our current website: https://www.trelmora.com
Updates

Our project has now been guaranteed! We look forward to finding the perfect design for our site pages!

Still waiting for a design that stands out from the rest and aligns with the creative brief.

Target Market(s)

Wedding Professionals and Engaged Couples

Industry/Entity Type

Wedding

Number of Pages Required

4 page

Font styles to use
Sans Serif

Colors
ffffff
fbd4d5
f59195
33a6d7
cadf82
86cfc6

Requirements
Must have
• Common sense stuff like having a unified brand that accurately represents our platform, speaks to our target market, and clearly articulates our vision
Nice to have
• Illustrations
Should not have
• Overly cheesy or childish. We want to be professional but still embrace the wedding culture.

```html
<!DOCTYPE html>
<html lang="en">
<head>
<meta charset="utf-8">
<title>Trelmora — Smarter Wed Planning</title>
<link href="https://fonts.googleapis.com/css2?family=Raleway:ital,wght@0,300;0,400;0,500;0,600;0,700;1,400&display=swap" rel="stylesheet">
<style>
:root{
  --pink:#f28a8e;
  --pink-deep:#e06f76;
  --pink-soft:#fbd4d5;
  --blue:#3ea6dc;
  --green:#cadf82;
  --paper:#f8f8f8;
  --ink:#3a3a3a;
  --white:#ffffff;
}
*{box-sizing:border-box;margin:0;padding:0}
html,body{width:1200px;height:3120px;overflow:hidden}
body{font-family:'Raleway',sans-serif;color:var(--ink);background:var(--white);position:relative}
.abs{position:absolute}

/* header */
.site-header{left:0;top:0;width:1200px;height:100px;background:var(--white)}
.brand{left:125px;top:20px;font-size:44px;font-weight:500;color:var(--blue)}
.main-nav{left:405px;top:40px;display:flex;gap:30px;font-size:13px;letter-spacing:.3px;color:#444}
.demo-btn{left:930px;top:25px;width:146px;height:48px;background:var(--pink);color:var(--white);font-size:11px;font-weight:600;display:flex;align-items:center;justify-content:center;border-radius:3px}

/* hero */
.hero{left:0;top:100px;width:1200px;height:500px;background:linear-gradient(100deg,#4b5a34 0%,#7c8a5a 30%,#c8b89a 55%,#d8cfc0 70%,#3f4a52 100%)}
.hero-title{left:0;top:310px;width:1200px;text-align:center;color:var(--white);font-size:30px;font-weight:300}
.hero-btn{left:485px;top:385px;width:230px;height:44px;border:2px solid var(--white);border-radius:24px;color:var(--white);font-size:13px;font-weight:600;display:flex;align-items:center;justify-content:center}
.hero-dots{left:570px;top:468px;display:flex;gap:8px;align-items:center}
.hero-dots span{width:10px;height:10px;border-radius:50%;background:var(--white)}
.hero-dots span.on{width:16px;height:16px;border:2px solid var(--white);background:transparent;box-shadow:inset 0 0 0 3px rgba(0,0,0,.15),inset 0 0 0 8px var(--white)}

/* section headings */
.section-heading{left:0;width:1200px;display:flex;justify-content:center;align-items:baseline;gap:14px;font-weight:600;color:var(--pink)}
.section-heading .brand-word{color:var(--blue);font-weight:500;font-size:1.15em}
.flourish{height:22px;width:200px;background:linear-gradient(90deg,transparent,var(--pink-soft) 20%,var(--pink) 50%,var(--pink-soft) 80%,transparent);border-radius:11px;opacity:.8}

/* welcome */
.welcome{left:0;top:600px;width:1200px;height:568px;background:var(--paper)}
.welcome-copy{left:120px;top:795px;width:575px;font-size:16px;line-height:27px;color:#444}
.welcome-copy p+p{margin-top:26px}
.read-more{left:120px;top:1083px;width:190px;height:40px;background:var(--pink);color:var(--white);font-size:15px;font-weight:700;display:flex;align-items:center;border-radius:3px}
.read-more .lbl{flex:1;padding-left:27px}
.read-more .arr{width:42px;border-left:1px solid rgba(255,255,255,.6);text-align:center;height:100%;display:flex;align-items:center;justify-content:center}
.welcome-photo{left:700px;top:835px;width:250px;height:250px;border-radius:50%;background:radial-gradient(circle at 40% 40%,#f4efe6,#c9b79a);box-shadow:0 4px 12px rgba(0,0,0,.25);border:4px solid var(--white)}
.welcome-photo-small{left:860px;top:815px;width:160px;height:160px;border-radius:50%;background:radial-gradient(circle at 45% 45%,#f3d59a,#b98a3a);box-shadow:0 4px 12px rgba(0,0,0,.25);border:4px solid var(--white)}

/* how to */
.howto{left:0;top:1168px;width:1200px;height:447px;background:linear-gradient(120deg,#e9a0a3,#d98b90 50%,#e7a2a4)}
.howto-title{left:0;top:1210px;width:1200px;text-align:center;color:var(--white);font-size:22px;font-weight:700}
.howto-rule{left:550px;top:1252px;width:100px;height:3px;background:var(--white)}
.step{left:155px;width:400px;display:flex;gap:22px;color:rgba(255,255,255,.55)}
.step.active{color:var(--white)}
.step-num{width:58px;height:58px;border:2px solid var(--green);display:flex;align-items:center;justify-content:center;font-size:28px;font-weight:700;flex:none}
.step.active .step-num{background:var(--pink-deep);color:var(--white)}
.step h3{font-size:19px;font-weight:700;margin-top:2px}
.step p{font-size:11px;font-weight:600;line-height:22px;margin-top:6px}
.tablet{left:665px;top:1290px;width:350px;height:270px;background:#f2f2f2;border:2px solid #ddd;border-radius:16px;box-shadow:0 3px 10px rgba(0,0,0,.2)}
.tablet-screen{left:696px;top:1318px;width:290px;height:212px;background:linear-gradient(#dfe7ef 0 10px,#fafafa 10px)}

/* why */
.why{left:0;top:1615px;width:1200px;height:470px;background:var(--paper)}
.feature{top:1835px;width:172px;height:222px;background:var(--white);border:5px solid var(--pink);text-align:center;padding:18px 8px}
.feature h4{font-size:15px;font-weight:600;line-height:21px;color:#333}
.feature p{font-size:13px;line-height:18px;color:#555;margin-top:14px}

/* services */
.services{left:0;top:2085px;width:1200px;height:660px;background:linear-gradient(180deg,#e08c8f,#d57a7f 60%,#e59597)}
.services-title{left:0;top:2118px;width:1200px;text-align:center;color:var(--white);font-size:42px;font-weight:300}
.service{width:260px;text-align:center}
.service-img{width:176px;height:176px;border-radius:50%;border:5px solid var(--white);margin:0 auto;box-shadow:0 3px 8px rgba(0,0,0,.25)}
.service-name{color:var(--white);font-size:20px;font-weight:700;margin-top:12px}
.to-top{left:995px;top:2700px;width:45px;height:45px;background:var(--pink);display:flex;align-items:center;justify-content:center}

/* footer */
.site-footer{left:0;top:2745px;width:1200px;height:375px;background:linear-gradient(#f07a80,#e6686f)}
.footer-nav{left:0;top:2765px;width:1200px;display:flex;justify-content:center;gap:20px;color:var(--white);font-size:18px;font-weight:700}
.footer-col{top:2820px;color:var(--white)}
.footer-col h5{font-size:17px;font-weight:700;margin-bottom:18px}
.gallery-list{list-style:none;font-size:14px;font-style:italic;line-height:21px;color:var(--pink-soft)}
.gallery-list li::before{content:"•";margin-right:8px}
.quote{display:flex;gap:22px}
.quote-mark{font-size:56px;line-height:44px;color:var(--white);font-family:Georgia,serif}
.quote p{font-size:14px;font-style:italic;line-height:21px;color:var(--pink-soft);width:140px}
.quote .who{margin-top:22px}
.contact{font-size:17px;line-height:22px;color:var(--pink-soft)}
.follow{margin-top:38px;font-size:17px;font-weight:700;color:var(--pink-soft)}
.socials{display:flex;gap:8px;margin-top:8px}
.socials span{width:32px;height:32px;border-radius:50%;background:var(--white)}
.footer-rule{left:0;top:3055px;width:1200px;border-top:2px dashed rgba(255,255,255,.7)}
.copyright{left:0;top:3078px;width:1200px;text-align:center;color:var(--white);font-size:17px}
</style>
</head>
<body>

<header class="site-header abs">
  <div class="brand abs">Trelmora</div>
  <nav class="main-nav abs"><span>ABOUT US</span><span>PROFESSIONALS</span><span>FEATURES</span><span>FOR COUPLES</span></nav>
  <div class="demo-btn abs">ACCESS DEMO</div>
</header>

<section class="hero abs" role="img" aria-label="Photo of a bride and groom under a floral wedding arch in a sunlit field"></section>
<h1 class="hero-title abs">Smarter Wed Planning™</h1>
<div class="hero-btn abs">Get Started</div>
<div class="hero-dots abs"><span class="on"></span><span></span><span></span></div>

<section class="welcome abs"></section>
<h2 class="section-heading abs" style="top:655px;font-size:46px">Welcome to <span class="brand-word">Trelmora</span></h2>
<div class="flourish abs" role="img" aria-label="Decorative floral flourish" style="left:500px;top:738px"></div>
<div class="welcome-copy abs">
  <p>Lorem ipsum dolor sit amet, consectetur adipiscing elit. Donec ut eros in nunc mollis ullamcorper sed vel ipsum. Nullam vitae varius justo. Donec placerat turpis laoreet, porttitor lectus sit amet, tempor purus. Vestibulum arcu lorem, pharetra vel dui eu, volutpat tincidunt nisl. Ut pretium nulla et egestas suscipit.</p>
  <p>Sed feugiat eget magna a vulputate. Vestibulum accumsan sodales ante, sit amet malesuada nunc molestie id. Cras sollicitudin est sed libero eleifend, eget finibus turpis dignissim. Donec in justo tincidunt, blandit enim sed, vestibulum nibh.</p>
</div>
<div class="read-more abs"><span class="lbl">READ MORE</span><span class="arr">»</span></div>
<div class="welcome-photo abs" role="img" aria-label="Photo of a decorated wedding reception table"></div>
<div class="welcome-photo-small abs" role="img" aria-label="Photo of two gold wedding rings"></div>

<section class="howto abs" role="img" aria-label="Soft pink background photo of wedding rings"></section>
<h2 class="howto-title abs">HOW TO GET STARTED</h2>
<div class="howto-rule abs"></div>
<div class="step active abs" style="top:1295px"><div class="step-num">1</div><div><h3>SIGN UP</h3><p>Create a free account on Trelmora to access popular collaboration tools.</p></div></div>
<div class="step abs" style="top:1393px"><div class="step-num">2</div><div><h3>COLLABORATE</h3><p>Add your venue and vendors within the application to start planning your special day.</p></div></div>
<div class="step abs" style="top:1491px"><div class="step-num">3</div><div><h3>CONNECT</h3><p>Unlock your team account within Trelmora to allow for seamless payments and budget management.</p></div></div>
<div class="tablet abs"></div>
<div class="tablet-screen abs" role="img" aria-label="Screenshot of the planning dashboard"></div>

<section class="why abs"></section>
<h2 class="section-heading abs" style="top:1660px;font-size:44px">Why <span class="brand-word">Trelmora</span></h2>
<div class="flourish abs" role="img" aria-label="Decorative floral flourish" style="left:500px;top:1750px"></div>
<div class="feature abs" style="left:121px"><h4>Saves Everyone Time</h4><p>Trelmora streamlines certain processes allowing you to spend more time on the things your want to or just relax!</p></div>
<div class="feature abs" style="left:316px"><h4>Better Client Reviews</h4><p>With Trelmora you can offer your clients an experience they will rave about, leading to better reviews and more clients.</p></div>
<div class="feature abs" style="left:514px"><h4>Accessible on Any Device</h4><p>Flexibility is key, which is why Trelmora's platform was built to be accessed on your phone, tablet or desktop.</p></div>
<div class="feature abs" style="left:709px"><h4>Simplified Organization</h4><p>Trelmora was built with organization in mind. All event details are in one place making executing an event easier.</p></div>
<div class="feature abs" style="left:905px"><h4>Lower Transaction Fees</h4><p>We offer the lowest online processing fees (2.85%) in the wedding industry, meaning you keep more of your money.</p></div>

<section class="services abs" role="img" aria-label="Pink-tinted photo of champagne glasses at a reception"></section>
<h2 class="services-title abs">Services We Offer</h2>
<div class="flourish abs" role="img" aria-label="Decorative floral flourish" style="left:500px;top:2188px;background:linear-gradient(90deg,transparent,rgba(255,255,255,.5) 30%,var(--white) 50%,rgba(255,255,255,.5) 70%,transparent)"></div>
<div class="service abs" style="left:185px;top:2238px"><div class="service-img" role="img" aria-label="Photo of colourful flower arrangements" style="background:radial-gradient(circle,#f3a3c0,#8fcf9a)"></div><div class="service-name">FLOWERS</div></div>
<div class="service abs" style="left:470px;top:2238px"><div class="service-img" role="img" aria-label="Photo of a tiered wedding cake" style="background:radial-gradient(circle,#ffffff,#d9cfd6)"></div><div class="service-name">WEDDING CAKES</div></div>
<div class="service abs" style="left:755px;top:2238px"><div class="service-img" role="img" aria-label="Photo of a bride portrait" style="background:radial-gradient(circle,#e9c3b4,#7a4a44)"></div><div class="service-name">PHOTOGRAPHY</div></div>
<div class="service abs" style="left:185px;top:2488px"><div class="service-img" role="img" aria-label="Photo of catered dishes" style="background:radial-gradient(circle,#f2d7b0,#b7845c)"></div><div class="service-name">CATER</div></div>
<div class="service abs" style="left:470px;top:2488px"><div class="service-img" role="img" aria-label="Photo of a decorated wedding car" style="background:radial-gradient(circle,#9a9aa4,#3c3c44)"></div><div class="service-name">WEDDING CARS</div></div>
<div class="service abs" style="left:755px;top:2488px"><div class="service-img" role="img" aria-label="Photo of a beach wedding venue" style="background:linear-gradient(#8fc9ee,#f3ede2 60%,#e58a8e)"></div><div class="service-name">WEDDING VENUE</div></div>
<div class="to-top abs"><svg width="20" height="14" viewBox="0 0 20 14"><path d="M2 12 L10 4 L18 12" fill="none" stroke="#fff" stroke-width="3"/></svg></div>

<footer class="site-footer abs"></footer>
<nav class="footer-nav abs"><span>ABOUT US</span><span>|</span><span>PROFESSIONALS</span><span>|</span><span>FEATURES</span><span>|</span><span>FOR COUPLES</span></nav>
<div class="footer-col abs" style="left:135px">
  <h5 style="margin-left:28px">IMAGE GALLERIES</h5>
  <ul class="gallery-list"><li>Wedding and Event Florals</li><li>Vintage Decorating</li><li>Interior Landscape</li><li>Holiday Decorating</li></ul>
</div>
<div class="footer-col abs" style="left:505px">
  <h5>RAVES AND REVIEWS</h5>
  <div class="quote"><span class="quote-mark">“</span><div><p>The flowers were beautiful and garnered many compliments. Thank you for the care and attention to detail.</p><p class="who">Jane Doe</p></div></div>
</div>
<div class="footer-col abs" style="left:860px">
  <h5>CONTACT INFO</h5>
  <div class="contact">34, Lorem Ipsum, St<br>info@trelmora.com<br>63.2500.0147</div>
  <div class="follow">Follows Us</div>
  <div class="socials"><span></span><span></span><span></span><span></span></div>
</div>
<div class="footer-rule abs"></div>
<div class="copyright abs">Trelmora ©2018 All Rights Reserved</div>

</body>
</html>
```